Brisel Home Care Brochure for Recruiting Clients

I need a brochure made for a home care company called 'Brisel Home Care'. I have uploaded the logo, location, and a few items about our company and what it offers. The final design should communicate trust and respect for patients and their families. I will probably be changing the phone number in the next few days so will need to add a new number and more serving locations.

Industry/Entity Type

Home Health Care

Colors
0555a3
ffffff
3176b5
85acd3
0392cd

Requirements
Must have
• Hello All,
• Thank you kindly for your patience. Please add the changes below to the brochures:
• Phone number: 571-555-0143
• Email: briselhc@quorvamail.com
• Homepage: [Non image link removed]Service Locations: Arlington County, Fairfax County, Fauquier County, Loudoun County, Prince William County
• Also please note the additional sentence at the end of the following key points:
• ABOUT US:
• Brisel serves to give patients the personal care they need in order for them to continue to live dignified and independent lives in the comfort of their homes. We begin by assessing and understanding our patient’s individual needs and met those needs through selectively assigning qualified, trustworthy and compassionate home care aids. Brisel holds great pride in keeping our client’s health, quality of life and well-being central in the design and delivery of our services. Our services can prevent re-hospitalization, postpone institutionalization, and reduce the need for urgent care.
• ABOUT OUR SERVICE PROVIDERS:
• We go through a rigorous in-depth application process with all of our service providers, so that you can rest assure that your home care provider is most qualified to meet your needs. Our application process also includes a thorough screening, criminal background check, DMV driving history and a comprehensive exam. Our service providers are trained, monitored, and tested continuously to meet our high standards of work ethic and professionalism. Our care providers are covered by professional liability, bonding, and workers’ compensation insurance. At Brisel teamwork among members is of key importance and it is how we conduct our day to day business. We work as a team with family, patient and their provider in developing an ideal care plan for the patient.
• OUR SERVICES:
• Companionship Services Include:
• - Offer companionship and conversation - Supervise home maintenance
• - Mail bills and letters
• - Provide reminders for appointments
• - Arrange appointments
• - Maintain calendar
• - Plan visits, outings and trips
• - Visit friends
• - Prepare grocery list
• - Assist with clothing selection
• - Stimulate mental awareness
• - Aid with reading
• - Monitor diet and eating
• - Check food expirations
• - Assist with morning and wake-up
• - Assist with evening and tuck-in
• - Provide respite care
• - Provide medication reminders
• - Assist with walking
• - Write letters and correspondence
• - Organize mail
• - Care for house plants
• - Answer the door
• - Assist with entertaining
• - Play games and cards
• - Rent and play movies
• - Oversee home deliveries
• - Supervise home maintenance
• - Discuss current and historical events - Reminisce about the past
• Home Helper Services Include:
• - Assist with laundry and ironing
• - Organize and clean closets
• - Assist with pet care
• - Attend social and sporting events - Accompany to lunch or dinner
• - Care for Alzhiemers
• - Change linens
• - Dust furniture
• - Drop off and pick up dry cleaning
• - Escort for shopping and errands
• - Escort to appointments
• - Escort to religious services
• - Help with airport task
• - Pick up prescriptions
• - Make beds
• - Prepare meals
• - Plan, prepare, and clean-up meals - Prepare future meals
• - Provide light housekeeping
• - Take out garbage
• Personal Services Include:
• - Ambulation
• - Bathing
• - Cognitive impairment - Mobility
• - Transferring
• - Incontinence
• - Dressing
• - Eating
• - Grooming
Nice to have
• Nice pictures of elderly clients with helpers or nurse.

```html
<!DOCTYPE html>
<html lang="en">
<head>
<meta charset="utf-8">
<title>Brisel Home Care – Tri-fold Brochure</title>
<link href="https://fonts.googleapis.com/css2?family=Open+Sans:ital,wght@0,400;0,600;0,700;1,400&family=Oswald:wght@400;500;600&display=swap" rel="stylesheet">
<style>
  :root {
    --brand-blue: #0ea5e9;
    --brand-blue-deep: #0392cd;
    --ink: #1f1f1f;
    --ink-soft: #2b2b2b;
    --paper: #ffffff;
    --stage: #ececec;
  }
  html, body {
    margin: 0;
    width: 1200px;
    height: 1200px;
    overflow: hidden;
    background: var(--stage);
  }
  .brochure {
    position: absolute;
    left: 50px;
    top: 208px;
    width: 1100px;
    height: 784px;
    background: var(--paper);
    overflow: hidden;
    font-family: "Open Sans", Arial, sans-serif;
    color: var(--ink);
  }
  .panel-bg { position: absolute; top: 0; height: 784px; }
  .panel-bg--inside { left: 0; width: 374px; background: linear-gradient(180deg, #fff 30%, #e9e9e9 100%); }
  .panel-bg--middle { left: 374px; width: 363px; background: linear-gradient(180deg, #f4f4f4 0%, #e6e6e6 100%); }
  .panel-bg--cover  { left: 737px; width: 363px; background: linear-gradient(180deg, #f6f6f6 0%, #e4e4e4 100%); }

  .artwork { position: absolute; left: 0; top: 0; }

  /* Inside panel */
  .section-title {
    position: absolute;
    left: 28px;
    margin: 0;
    font-weight: 700;
    font-size: 17px;
    line-height: 22px;
    color: var(--brand-blue-deep);
  }
  .body-copy {
    position: absolute;
    left: 28px;
    width: 318px;
    margin: 0;
    font-style: italic;
    font-size: 9.6px;
    line-height: 13.2px;
    text-align: justify;
    color: var(--ink);
  }
  .about-title { top: 278px; }
  .about-copy { top: 303px; }
  .providers-title { top: 482px; }
  .providers-copy { top: 507px; }

  /* Middle panel */
  .location {
    position: absolute;
    left: 374px;
    width: 363px;
    top: 46px;
    margin: 0;
    text-align: center;
    color: var(--paper);
    font-size: 15px;
    line-height: 21px;
  }
  .location__label { display: block; color: var(--ink); font-weight: 700; font-size: 16px; }

  .services {
    position: absolute;
    left: 392px;
    width: 327px;
    top: 304px;
  }
  .services__title {
    margin: 0 0 4px;
    text-align: center;
    font-weight: 700;
    font-size: 14px;
    line-height: 18px;
    color: var(--brand-blue-deep);
  }
  .services__group {
    margin: 0 0 4px;
    font-size: 8.6px;
    line-height: 11.2px;
    text-align: justify;
    color: var(--ink);
  }
  .services__label { font-weight: 700; color: var(--brand-blue-deep); }

  .contact-box {
    position: absolute;
    left: 427px;
    top: 556px;
    width: 257px;
    height: 132px;
    box-sizing: border-box;
    border: 3px solid var(--ink);
    border-radius: 20px;
    background: linear-gradient(180deg, #38c0f5 0%, var(--brand-blue) 100%);
    text-align: center;
    font-family: "Oswald", "Arial Narrow", sans-serif;
    padding-top: 18px;
  }
  .contact-box__title { display: block; font-size: 23px; font-weight: 500; line-height: 28px; color: var(--ink); }
  .contact-box__phone { display: block; font-size: 32px; font-weight: 500; line-height: 38px; color: var(--paper); }
  .contact-box__email { display: block; font-size: 13px; font-weight: 500; line-height: 22px; color: var(--ink); }

  .visit {
    position: absolute;
    left: 374px;
    width: 363px;
    top: 704px;
    margin: 0;
    text-align: center;
    font-size: 16px;
    line-height: 23px;
    color: var(--ink);
  }
  .visit__url { display: block; font-weight: 700; font-size: 17px; color: var(--brand-blue-deep); }

  /* Cover panel */
  .brand {
    position: absolute;
    left: 730px;
    top: 48px;
    display: flex;
    align-items: center;
  }
  .brand__mark {
    width: 76px;
    height: 76px;
    border-radius: 50%;
    background: var(--brand-blue);
    margin-right: 12px;
    flex: none;
  }
  .brand__name {
    display: block;
    font-family: "Oswald", "Arial Narrow", sans-serif;
    font-weight: 500;
    font-size: 34px;
    line-height: 40px;
    color: var(--brand-blue);
  }
  .brand__url {
    display: block;
    font-family: "Oswald", "Arial Narrow", sans-serif;
    font-size: 22px;
    line-height: 30px;
    color: var(--ink-soft);
  }

  .cover-headline {
    position: absolute;
    right: 45px;
    top: 594px;
    margin: 0;
    text-align: right;
    font-family: "Oswald", "Arial Narrow", sans-serif;
    font-weight: 600;
  }
  .cover-headline__top { display: block; font-size: 60px; line-height: 66px; color: var(--ink); }
  .cover-headline__bottom { display: block; font-size: 38px; line-height: 44px; font-weight: 500; color: var(--brand-blue); }
  .cover-url {
    position: absolute;
    right: 45px;
    width: 320px;
    top: 712px;
    margin: 0;
    text-align: center;
    font-size: 15px;
    color: var(--ink-soft);
  }

  .footer-bar { position: absolute; bottom: 0; height: 18px; }
  .footer-bar--inside { left: 0; width: 374px; background: var(--brand-blue); }
  .footer-bar--middle { left: 374px; width: 363px; background: var(--ink); }
  .footer-bar--cover { left: 737px; width: 363px; background: var(--brand-blue); }
</style>
</head>
<body>
<main class="brochure">
  <div class="panel-bg panel-bg--inside"></div>
  <div class="panel-bg panel-bg--middle"></div>
  <div class="panel-bg panel-bg--cover"></div>

  <svg class="artwork" width="1100" height="784" viewBox="0 0 1100 784">
    <defs>
      <linearGradient id="warmPhoto" x1="0" y1="0" x2="1" y2="1">
        <stop offset="0" stop-color="#efe6e0"/>
        <stop offset="0.5" stop-color="#d9c4ba"/>
        <stop offset="1" stop-color="#b98f88"/>
      </linearGradient>
      <linearGradient id="coolPhoto" x1="0" y1="0" x2="1" y2="1">
        <stop offset="0" stop-color="#e9ecef"/>
        <stop offset="0.5" stop-color="#c8d3de"/>
        <stop offset="1" stop-color="#7d9cc4"/>
      </linearGradient>
      <linearGradient id="blueBlock" x1="0" y1="0" x2="0" y2="1">
        <stop offset="0" stop-color="#0aa6ee"/>
        <stop offset="1" stop-color="#20b6f3"/>
      </linearGradient>
    </defs>

    <path fill="url(#blueBlock)" d="M374,0 H640 C690,60 690,170 760,210 C700,222 640,250 560,272 C500,290 440,295 374,262 Z"/>
    <path fill="#0ea5e9" d="M0,250 C70,220 140,205 210,210 C290,218 340,250 374,262 C440,295 500,290 560,272 L560,284 C500,302 440,308 374,280 C320,258 270,238 200,236 C120,234 60,258 0,284 Z"/>
    <path fill="none" stroke="#1f1f1f" stroke-width="7" d="M0,262 C70,232 140,218 210,222 C290,230 340,260 380,275 C440,300 500,296 560,278"/>
    <path role="img" aria-label="Photo of a carer tucking a blanket around an elderly woman" fill="url(#warmPhoto)" d="M0,0 H374 V255 C330,232 280,212 210,208 C140,204 70,222 0,250 Z"/>

    <path fill="#0ea5e9" d="M640,0 C690,60 690,170 760,210 C860,262 980,246 1100,285 V302 C980,266 860,282 752,228 C670,188 678,60 620,0 Z"/>
    <path fill="none" stroke="#1f1f1f" stroke-width="6" d="M632,0 C682,60 684,170 756,218 C860,272 980,258 1100,296"/>

    <path role="img" aria-label="Photo of a smiling nurse holding hands with an elderly woman in a wheelchair" fill="url(#coolPhoto)" d="M737,228 C760,240 800,252 840,258 C940,272 1020,270 1100,300 V532 C1040,548 980,558 920,548 C860,540 800,512 737,512 Z"/>
    <path fill="#0ea5e9" d="M737,500 C800,500 860,530 920,540 C980,550 1040,540 1100,522 V548 C1040,568 980,574 920,566 C860,556 800,526 737,524 Z"/>
    <path fill="none" stroke="#1f1f1f" stroke-width="5" d="M737,514 C800,514 860,542 920,552 C980,562 1040,552 1100,534"/>
  </svg>

  <h2 class="section-title about-title">ABOUT US:</h2>
  <p class="body-copy about-copy">Brisel serves to give patients the personal care they need in order for them to continue to live dignified and independent lives in the comfort of their homes. We begin by assessing and understanding our patient’s individual needs and met those needs through selectively assigning qualified, trustworthy and compassionate home care aids. Brisel holds great pride in keeping our client’s health, quality of life and well-being central in the design and delivery of our services. Our services can prevent re-hospitalization, postpone institutionalization, and reduce the need for urgent care.</p>

  <h2 class="section-title providers-title">ABOUT OUR SERVICE PROVIDERS</h2>
  <p class="body-copy providers-copy">We go through a rigorous in-depth application process with all of our service providers, so that you can rest assure that your home care provider is most qualified to meet your needs. Our application process also includes a thorough screening, criminal background check, DMV driving history and a comprehensive exam. Our service providers are trained, monitored, and tested continuously to meet our high standards of work ethic and professionalism. Our care providers are covered by professional liability, bonding, and workers’ compensation insurance. At Brisel teamwork among members is of key importance and it is how we conduct our day to day business. We work as a team with family, patient and their provider in developing an ideal care plan for the patient.</p>

  <p class="location">
    <span class="location__label">LOCATION:</span>
    512 Wexler Lane,<br>
    Falls Church, VA 22046<br>
    Serving the following counties:<br>
    Arlington, Fairfax, Fauquier,<br>
    Loudoun and Prince William
  </p>

  <section class="services">
    <h2 class="services__title">OUR SERVICES</h2>
    <p class="services__group"><span class="services__label">Companionship:</span> companionship and conversation · mail bills and letters · appointment reminders · arrange appointments · maintain calendar · plan visits, outings and trips · visit friends · prepare grocery list · clothing selection · stimulate mental awareness · aid with reading · monitor diet and eating · check food expirations · morning wake-up · evening tuck-in · respite care · medication reminders · assist with walking · write letters and correspondence · organize mail · care for house plants · answer the door · assist with entertaining · play games and cards · rent and play movies · oversee home deliveries · supervise home maintenance · discuss current and historical events · reminisce about the past</p>
    <p class="services__group"><span class="services__label">Home Helper:</span> laundry and ironing · organize and clean closets · pet care · attend social and sporting events · accompany to lunch or dinner · care for Alzheimer’s · change linens · dust furniture · dry cleaning drop-off and pick-up · escort for shopping, errands, appointments and religious services · help with airport tasks · pick up prescriptions · make beds · plan, prepare and clean up meals · prepare future meals · light housekeeping · take out garbage</p>
    <p class="services__group"><span class="services__label">Personal:</span> ambulation · bathing · cognitive impairment · mobility · transferring · incontinence · dressing · eating · grooming</p>
  </section>

  <div class="contact-box">
    <span class="contact-box__title">CONTACT US NOW!</span>
    <span class="contact-box__phone">571-555-0143</span>
    <span class="contact-box__email">EMAIL: BRISELHC@QUORVAMAIL.COM</span>
  </div>

  <p class="visit">Visit us to know more at:<span class="visit__url">www.briselhomecare-va.org</span></p>

  <div class="brand">
    <div class="brand__mark"></div>
    <div>
      <span class="brand__name">BRISEL HOME CARE</span>
      <span class="brand__url">www.briselhomecare-va.org</span>
    </div>
  </div>

  <h1 class="cover-headline">
    <span class="cover-headline__top">WE WORK AS</span>
    <span class="cover-headline__bottom">A TEAM WITH FAMILY</span>
  </h1>
  <p class="cover-url">www.briselhomecare-va.org</p>

  <div class="footer-bar footer-bar--inside"></div>
  <div class="footer-bar footer-bar--middle"></div>
  <div class="footer-bar footer-bar--cover"></div>
</main>
</body>
</html>
```